Plumbing Company After Business Card

Business card for a plumbing business that offers a variety of plumbing services including maintenance, domestic and commercial plumbing. My main focus is to offer high quality professional service. A logo on the card would be ideal. Any other questions feel free to email. Cheers

Looking for something modern and upmarket with preferably a matte black background

Business name is Crestline Plumbing and Gas

Industry/Entity Type

Plumbing

Contact Information for Business Card

Crestline Plumbing and Gas
Marcus Thorvale
0472519306
14 Karrabee Drive, Ascot 3550
crestlineplumbing@mailbay.com.au
ABN 64 915 207 338

Font styles to use
Sans Serif

Colors
1b1b1b
ffffff
3377b5

Requirements
Must have
• Domestic
• Commercial
• Maintenance

```html
<!DOCTYPE html>
<html lang="en">
<head>
<meta charset="utf-8">
<title>Crestline Plumbing and Gas — Business Card</title>
<link rel="stylesheet" href="https://fonts.googleapis.com/css2?family=Arimo:wght@400;700&display=swap">
<style>
  :root {
    --card-black: #1b1b1b;
    --ink-white: #ffffff;
    --brand-blue: #3377b5;
    --stage: #5e5e5e;
  }
  * { margin: 0; padding: 0; box-sizing: border-box; }
  html, body {
    width: 1200px; height: 1000px; overflow: hidden;
    background: var(--stage);
    font-family: "Arimo", Arial, sans-serif;
    color: var(--ink-white);
  }
  .canvas { position: relative; width: 1200px; height: 1000px; }
  .card {
    position: absolute; left: 327px; width: 562px; height: 347px;
    background: var(--card-black);
    overflow: hidden;
  }
  .card--front { top: 103px; }
  .card--back { top: 533px; }

  .wordmark { position: absolute; display: flex; align-items: center; gap: 10px; }
  .wordmark__dot {
    width: 34px; height: 34px; border-radius: 50%;
    background: var(--brand-blue); flex: none;
  }
  .wordmark__text { font-weight: 700; color: var(--ink-white); line-height: 1; }
  .wordmark__name { display: block; font-size: 36px; letter-spacing: 1px; }
  .wordmark__sub { display: block; font-size: 14px; margin-top: 4px; text-align: right; }
  .card--front .wordmark { left: 50px; top: 62px; }
  .card--back .wordmark { left: 74px; top: 146px; }

  .contact-panel { position: absolute; left: 0; top: 0; width: 562px; height: 347px; }
  .contact {
    position: absolute; left: 303px; top: 130px;
  }
  .contact__name { font-size: 20px; font-weight: 700; letter-spacing: 0.8px; margin-bottom: 16px; }
  .contact__line { font-size: 13.5px; font-weight: 400; line-height: 23.5px; }

  .divider { position: absolute; left: 303px; top: 52px; }
  .services {
    position: absolute; left: 335px; top: 126px;
    list-style: none; font-size: 19px; font-weight: 700; letter-spacing: 0.8px;
  }
  .services li { line-height: 32.5px; }
</style>
</head>
<body>
<main class="canvas">
  <section class="card card--front" aria-label="Business card front">
    <div class="wordmark">
      <span class="wordmark__dot"></span>
      <span class="wordmark__text">
        <span class="wordmark__name">Crestline</span>
        <span class="wordmark__sub">Plumbing and Gas</span>
      </span>
    </div>
    <svg class="contact-panel" viewBox="0 0 562 347" aria-hidden="true">
      <path d="M286 347 V110 C286 40 330 0 400 0 H508 V240 C508 310 470 347 410 347 Z" fill="var(--brand-blue)"/>
    </svg>
    <div class="contact">
      <p class="contact__name">Marcus Thorvale</p>
      <p class="contact__line">0472519306</p>
      <p class="contact__line">14 Karrabee Drive, Ascot 3550</p>
      <p class="contact__line">crestlineplumbing@mailbay.com.au</p>
      <p class="contact__line">ABN 64 915 207 338</p>
    </div>
  </section>

  <section class="card card--back" aria-label="Business card back">
    <div class="wordmark">
      <span class="wordmark__dot"></span>
      <span class="wordmark__text">
        <span class="wordmark__name">Crestline</span>
        <span class="wordmark__sub">Plumbing and Gas</span>
      </span>
    </div>
    <svg class="divider" width="3" height="230" viewBox="0 0 3 230" aria-hidden="true">
      <defs>
        <linearGradient id="divider-fade" x1="0" y1="0" x2="0" y2="1">
          <stop offset="0" stop-color="#3377b5" stop-opacity="0"/>
          <stop offset="0.5" stop-color="#3377b5" stop-opacity="1"/>
          <stop offset="1" stop-color="#3377b5" stop-opacity="0"/>
        </linearGradient>
      </defs>
      <rect width="3" height="230" fill="url(#divider-fade)"/>
    </svg>
    <ul class="services">
      <li>Domestic</li>
      <li>Commercial</li>
      <li>Maintenance</li>
    </ul>
  </section>
</main>
</body>
</html>
```